Pelin Thai Massage Double Sided Flyer Luxury

I require a double sided flyer
we are a Thai Massage Spa
Would like gold, deep purple and bronze colours
Something eye catching and looks professional

```html
<!DOCTYPE html>
<html lang="en">
<head>
<meta charset="utf-8">
<title>Pelin Thai Massage – Double Sided Flyer</title>
<link rel="stylesheet" href="https://fonts.googleapis.com/css2?family=Marcellus&family=Playfair+Display:ital,wght@0,700;1,400&family=Raleway:wght@400;500&family=Ribeye&display=swap">
<style>
  :root {
    --page-bg: #3b2b23;
    --gold: #f2c14e;
    --gold-light: #ffe08a;
    --gold-deep: #d99a1c;
    --bronze-dark: #2a1208;
    --bronze: #4a2614;
    --ink: #2b1a12;
    --body-grey: #3d3d3d;
    --white: #ffffff;
    --leaf: #2f8a2c;
    --leaf-dark: #1d5e1c;
    --voucher-green: #2d7d3a;
  }
  * { margin: 0; padding: 0; box-sizing: border-box; }
  html, body { width: 1200px; height: 848px; overflow: hidden; }
  body { background: var(--page-bg); position: relative; }

  .flyer {
    position: absolute; top: 112px; width: 436px; height: 617px; overflow: hidden;
    box-shadow: 0 10px 30px rgba(0,0,0,.45);
  }
  .flyer--front { left: 99px; background: var(--white); }
  .flyer--back { left: 633px; background: radial-gradient(ellipse at 50% 70%, #4a2414 0%, var(--bronze-dark) 70%); }

  /* Front */
  .hero-photo {
    position: absolute; left: 0; top: 0; width: 436px; height: 370px;
    background:
      linear-gradient(to bottom, rgba(255,255,255,0) 62%, #fff 100%),
      radial-gradient(ellipse 120px 90px at 30% 22%, rgba(60,42,40,.75) 0%, rgba(60,42,40,0) 100%),
      radial-gradient(ellipse 150px 120px at 32% 52%, rgba(232,176,148,.95) 0%, rgba(232,176,148,0) 100%),
      radial-gradient(ellipse 220px 70px at 45% 76%, rgba(236,190,168,.9) 0%, rgba(236,190,168,0) 100%),
      radial-gradient(ellipse 120px 160px at 82% 50%, rgba(70,70,90,.55) 0%, rgba(70,70,90,0) 100%),
      radial-gradient(ellipse 200px 120px at 58% 12%, rgba(214,200,240,.95) 0%, rgba(214,200,240,0) 100%),
      linear-gradient(115deg, #b8c2e6 0%, #dcd8ef 45%, #c9cde6 100%);
  }
  .front-brand-mark {
    position: absolute; left: 276px; top: 42px; width: 86px; height: 86px; border-radius: 50%;
    border: 4px solid var(--gold);
  }
  .front-brand {
    position: absolute; left: 219px; top: 133px; width: 200px; text-align: center;
    font: 400 17px "Raleway", sans-serif; color: var(--gold); white-space: nowrap;
  }
  .front-headline {
    position: absolute; left: 0; top: 311px; width: 436px; text-align: center;
    font: 400 22px/25px "Marcellus", serif; color: var(--ink);
  }
  .welcome-pill {
    position: absolute; left: 28px; top: 374px; width: 372px; height: 39px; border-radius: 20px;
    background: linear-gradient(to bottom, #6b3a1f 0%, var(--bronze-dark) 55%, #1a0904 100%);
    box-shadow: 0 2px 4px rgba(0,0,0,.3);
    display: flex; align-items: center; justify-content: center;
    font: 400 23px "Ribeye", serif; letter-spacing: 1px; color: var(--gold);
  }
  .front-copy {
    position: absolute; left: 0; top: 430px; width: 436px; text-align: center; white-space: nowrap;
    font: 400 11.2px/13.6px "Raleway", sans-serif; color: var(--body-grey);
  }
  .front-copy p + p { margin-top: 13.6px; }
  .front-wave { position: absolute; left: 0; bottom: 0; }
  .front-url {
    position: absolute; right: 30px; bottom: 16px;
    font: 400 14px "Marcellus", serif; color: var(--gold);
  }

  /* Back */
  .back-photo {
    position: absolute; left: 0; top: 0; width: 436px; height: 180px;
    background: linear-gradient(100deg, #3a1a0c 0%, #6a3a22 35%, #8a5a40 65%, #4a2a18 100%);
  }
  .back-top-wave { position: absolute; left: 0; top: 110px; }
  .back-title {
    position: absolute; left: 0; top: 22px; width: 436px; text-align: center;
    font: 700 27px "Playfair Display", serif; color: var(--gold); font-variant-numeric: lining-nums;
  }
  .back-intro {
    position: absolute; left: 0; top: 59px; width: 436px; text-align: center;
    font: 400 14px/15.5px "Raleway", sans-serif; color: var(--white);
  }
  .service-pill {
    position: absolute; height: 26px; border-radius: 13px;
    background: linear-gradient(to bottom, var(--gold-light), var(--gold) 50%, var(--gold-deep));
    display: flex; align-items: center; justify-content: center; gap: 8px;
    font: 700 13px "Playfair Display", serif; color: var(--ink); letter-spacing: .3px;
  }
  .service-pill__dot { width: 14px; height: 14px; border-radius: 50%; border: 1.5px solid var(--ink); }
  .service-pill--tissue { left: 111px; top: 191px; width: 201px; }
  .service-pill--floor { left: 62px; top: 305px; width: 299px; }
  .price { position: absolute; font: 700 18px "Playfair Display", serif; color: var(--white); font-variant-numeric: lining-nums; white-space: nowrap; }
  .price-note { position: absolute; font: 400 12px/15.5px "Raleway", sans-serif; color: var(--gold); white-space: nowrap; }
  .price--60 { right: 229px; top: 232px; }
  .price-note--60 { right: 229px; top: 256px; text-align: right; }
  .price--90 { left: 224px; top: 232px; }
  .price-note--90 { left: 224px; top: 256px; }
  .price-divider { position: absolute; left: 212px; top: 237px; width: 1px; height: 46px; background: var(--gold); }
  .price--floor { left: 0; width: 436px; text-align: center; top: 344px; }
  .price-note--floor { left: 0; width: 436px; text-align: center; top: 367px; }

  .back-bottom-wave { position: absolute; left: 0; top: 440px; }
  .voucher {
    position: absolute; left: 84px; top: 413px; width: 254px; height: 104px; background: var(--white);
  }
  .voucher__gift { position: absolute; left: 74px; top: 52px; font: 400 6px "Raleway", sans-serif; color: var(--voucher-green); }
  .voucher__title { position: absolute; left: 8px; top: 55px; font: italic 400 19px "Playfair Display", serif; color: var(--voucher-green); }
  .voucher__terms { position: absolute; left: 10px; top: 78px; width: 114px; font: 400 2.6px/3.2px "Raleway", sans-serif; color: #555; }
  .voucher__art {
    position: absolute; left: 133px; top: 10px; width: 104px; height: 86px;
    background: linear-gradient(135deg, #5bb845 0%, var(--leaf) 45%, var(--leaf-dark) 100%);
  }
  .voucher__discount { position: absolute; left: 160px; top: 28px; width: 80px; text-align: center; color: var(--white); }
  .voucher__percent { display: block; font: italic 400 27px/28px "Playfair Display", serif; font-variant-numeric: lining-nums; }
  .voucher__label { display: block; font: italic 400 8px "Playfair Display", serif; letter-spacing: .5px; }

  .open-pill {
    position: absolute; left: 82px; top: 520px; width: 258px; height: 28px; border-radius: 14px;
    background: linear-gradient(to bottom, var(--gold-light), var(--gold) 50%, var(--gold-deep));
    display: flex; align-items: center; justify-content: center;
    font: 700 20px "Playfair Display", serif; color: var(--ink); font-variant-numeric: lining-nums;
  }
  .footer-mark { position: absolute; left: 20px; top: 566px; width: 30px; height: 30px; border-radius: 50%; border: 2px solid var(--bronze); }
  .footer-name { position: absolute; left: 68px; top: 558px; font: 400 17px "Marcellus", serif; color: var(--ink); letter-spacing: .5px; white-space: nowrap; }
  .footer-address { position: absolute; left: 68px; top: 580px; font: 400 12.5px "Marcellus", serif; color: var(--ink); white-space: nowrap; }
  .footer-phone { position: absolute; left: 279px; top: 557px; font: 400 19.5px "Marcellus", serif; color: var(--ink); white-space: nowrap; }
  .footer-url { position: absolute; left: 280px; top: 581px; font: 400 12.5px "Marcellus", serif; color: var(--ink); white-space: nowrap; }
</style>
</head>
<body>

<section class="flyer flyer--front">
  <div class="hero-photo" role="img" aria-label="Photo of a smiling woman lying on a massage table receiving a back massage from a therapist, with frangipani flowers"></div>
  <div class="front-brand-mark"></div>
  <div class="front-brand">Pelin Thai Massage</div>
  <h1 class="front-headline">Pain Does't Have To Be A<br>Normal Way Of Life!</h1>
  <div class="welcome-pill">WELCOME TO LUXURY</div>
  <div class="front-copy">
    <p>Set in the heart of Oakmere, Pelin Thai Massage will allow<br>you to immerse yourself in a place where your wellbeing &amp; rejuvena-<br>tion is at the centre of what we do.</p>
    <p>Using Thai traditions, our highly trained therapists offer<br>revitalising body treatments with their deep tissue massage tech-<br>niques. In their hands, you will see and feel immediate results.</p>
  </div>
  <svg class="front-wave" width="436" height="70" viewBox="0 0 436 70" aria-hidden="true">
    <path d="M0 0 C30 40 110 48 200 34 C290 20 360 10 436 26 L436 70 L0 70 Z" fill="#fbe7a8"/>
    <path d="M0 0 C30 44 110 52 200 38 C290 24 360 14 436 30 L436 70 L0 70 Z" fill="#f2c14e"/>
    <path d="M0 4 C30 52 120 58 210 44 C300 30 370 22 436 34 L436 70 L0 70 Z" fill="#ffffff"/>
    <path d="M0 8 C30 56 120 62 210 48 C300 34 370 26 436 38 L436 70 L0 70 Z" fill="#2a1208"/>
  </svg>
  <div class="front-url">PelinThaiMassage.co.uk</div>
</section>

<section class="flyer flyer--back">
  <div class="back-photo" role="img" aria-label="Photo of a woman relaxing during a shoulder massage beside candles and spa stones"></div>
  <svg class="back-top-wave" width="436" height="80" viewBox="0 0 436 80" aria-hidden="true">
    <path d="M0 50 C70 78 140 70 220 45 C300 20 380 14 436 36 L436 80 L0 80 Z" fill="#f2c14e"/>
    <path d="M0 56 C70 82 140 76 220 52 C300 28 380 22 436 44 L436 80 L0 80 Z" fill="#2a1208"/>
  </svg>
  <h2 class="back-title">MASSAGES</h2>
  <p class="back-intro">Restore balance. Revive your senses.<br>Discover all the ways Pelin Thai Massage can<br>breathe new life into your body &amp; soul.</p>

  <div class="service-pill service-pill--tissue"><span class="service-pill__dot"></span>DEEP TISSUE MASSAGE</div>
  <div class="price price--60">60 MINUTES £45</div>
  <div class="price-note price-note--60">Oil massage personalised<br>light to firm pressure</div>
  <div class="price-divider"></div>
  <div class="price price--90">90 MINUTES £55</div>
  <div class="price-note price-note--90">Oil massage, medium to<br>firm pressure</div>

  <div class="service-pill service-pill--floor"><span class="service-pill__dot"></span>THAI FLOOR TRADTIONAL MASSAGE</div>
  <div class="price price--floor">60 MINUTES £45</div>
  <div class="price-note price-note--floor">Dry massage, medium to firm pressure<br>applying stretching technique</div>

  <svg class="back-bottom-wave" width="436" height="177" viewBox="0 0 436 177" aria-hidden="true">
    <defs>
      <linearGradient id="silverFill" x1="0" y1="0" x2="1" y2="0">
        <stop offset="0" stop-color="#bdbdbd"/>
        <stop offset="0.5" stop-color="#f2f2f2"/>
        <stop offset="1" stop-color="#bdbdbd"/>
      </linearGradient>
    </defs>
    <path d="M0 40 C30 75 70 92 120 96 L300 96 C340 40 400 10 436 44 L436 177 L0 177 Z" fill="#f2c14e"/>
    <path d="M0 44 C30 79 70 96 120 100 L300 100 C340 46 400 18 436 50 L436 177 L0 177 Z" fill="url(#silverFill)"/>
  </svg>

  <div class="voucher">
    <span class="voucher__gift">GIFT</span>
    <span class="voucher__title">VOUCHER</span>
    <p class="voucher__terms">Present this voucher at reception to receive half off any treatment. Valid for one person. Not exchangeable for cash. Booking required in advance.</p>
    <div class="voucher__art" role="img" aria-label="Illustration of large green leaves"></div>
    <div class="voucher__discount">
      <span class="voucher__percent">50%</span>
      <span class="voucher__label">DISCOUNT</span>
    </div>
  </div>

  <div class="open-pill">OPEN 7 DAYS A WEEK</div>
  <div class="footer-mark"></div>
  <div class="footer-name">PELIN THAI MASSAGE</div>
  <div class="footer-address">12 Willow Row, Brackton, BT4 2QE</div>
  <div class="footer-phone">0100 555 0192</div>
  <div class="footer-url">PelinThaiMassage.co.uk</div>
</section>

</body>
</html>
```